Brightwell Amusements Investor Brochure

Start Up Company Brightwell Amusements requires 4 page A4 size brochure outlining and detailing new product. Draft layout attached. Information and points of difference included. Company logo and graphics attached. Final design should sell to investors.

```html
<!DOCTYPE html>
<html lang="en">
<head>
<meta charset="utf-8">
<title>Brightwell Amusements Investor Brochure</title>
<link href="https://fonts.googleapis.com/css2?family=Oswald:wght@500;700&family=Open+Sans:wght@400;600;700&display=swap" rel="stylesheet">
<style>
  :root {
    --navy: #1f3a8c;
    --navy-deep: #16296b;
    --blue: #2f57b5;
    --sky: #6f9ee0;
    --pale: #dfe4f5;
    --red: #e3161d;
    --ink: #2b2b3a;
    --paper: #ffffff;
    --backdrop: #ececec;
  }
  * { box-sizing: border-box; margin: 0; padding: 0; }
  html, body { width: 971px; height: 1200px; overflow: hidden; }
  body { background: var(--backdrop); font-family: "Open Sans", sans-serif; color: var(--ink); position: relative; }
  .page { position: absolute; width: 410px; height: 520px; background: var(--paper); overflow: hidden; box-shadow: 0 2px 8px rgba(0,0,0,.18); }
  .page-travellers { left: 60px; top: 73px; }
  .page-airports { left: 491px; top: 73px; }
  .page-global { left: 60px; top: 608px; }
  .page-hospitals { left: 491px; top: 608px; }
  .abs { position: absolute; }
  .headline { font-family: "Oswald", sans-serif; font-weight: 700; line-height: 1.05; text-transform: uppercase; }
  .sub { font-family: "Oswald", sans-serif; font-weight: 500; line-height: 1.2; }
  .placeholder { position: absolute; border-radius: 6px; }
  .brand { display: flex; align-items: center; gap: 10px; }
  .brand-mark { width: 30px; height: 30px; border: 3px solid currentColor; border-radius: 4px; flex: none; }
  .brand-name { font-family: "Oswald", sans-serif; font-weight: 700; text-transform: uppercase; line-height: 1; }

  /* page 1 */
  .page-travellers { background: var(--navy); }
  .page-travellers .top-band { position: absolute; left: 0; top: 0; }
  .page-travellers .headline { left: 24px; top: 18px; font-size: 27px; color: var(--red); }
  .page-travellers .sub { left: 24px; top: 52px; font-size: 17px; color: #2c3559; }
  .page-travellers .brand { left: 42px; top: 182px; color: #fff; }
  .page-travellers .brand-name { font-size: 25px; }
  .page-travellers .photo { left: 25px; top: 255px; width: 358px; height: 212px; background: linear-gradient(180deg,#c9cfd9,#8e97a6 60%,#c4b9a8); }

  /* page 2 */
  .page-airports .headline { left: 26px; top: 22px; font-size: 26px; color: var(--red); }
  .page-airports .headline.second { top: 52px; color: var(--navy); }
  .page-airports .map { left: 140px; top: 100px; width: 250px; height: 210px; background: radial-gradient(circle at 50% 55%, #7aa5e6, #5d8ad6); border-radius: 40% 45% 35% 40%; }
  .bullets { left: 18px; top: 120px; width: 112px; list-style: none; font-size: 6.5px; line-height: 1.35; }
  .bullets li { position: relative; padding-left: 9px; margin-bottom: 6px; }
  .bullets li::before { content: ""; position: absolute; left: 0; top: 2px; width: 5px; height: 5px; background: var(--blue); border-radius: 50%; }
  .kiosk { background: linear-gradient(180deg, var(--blue), var(--navy-deep)); border-radius: 10px 10px 4px 4px; }
  .page-airports .kiosk { left: 30px; top: 250px; width: 82px; height: 250px; }
  .stat { left: 135px; top: 330px; width: 265px; text-align: center; font-family: "Oswald", sans-serif; font-weight: 500; font-size: 13px; color: #3b4158; line-height: 1.25; }
  .stat-note { left: 135px; top: 365px; width: 265px; text-align: center; font-size: 5.5px; font-weight: 700; }
  .data-table { border-collapse: collapse; color: #fff; }
  .airport-table { left: 135px; top: 380px; width: 265px; background: var(--navy); font-size: 5px; line-height: 1.2; }
  .airport-table td { padding: 2.5px 4px; border-bottom: 1px solid rgba(255,255,255,.25); }
  .airport-table td.num { text-align: right; }

  /* page 3 */
  .page-global .headline { left: 0; width: 100%; text-align: center; top: 32px; font-size: 21px; color: var(--red); }
  .page-global .map { left: 42px; top: 92px; width: 330px; height: 125px; background: linear-gradient(90deg, var(--navy), var(--blue), var(--navy)); border-radius: 30px; }
  .page-global .sub.small { left: 0; width: 100%; text-align: center; top: 230px; font-size: 10px; color: #3b3b4a; }
  .page-global .sub.big { left: 0; width: 100%; text-align: center; top: 245px; font-size: 20px; color: var(--navy); font-weight: 700; }
  .chart { left: 28px; top: 280px; width: 352px; height: 240px; background: linear-gradient(180deg, #3e5ab0, var(--navy-deep)); border-radius: 4px; }
  .chart-row { position: absolute; left: 0; height: 10px; font-size: 5.5px; color: #dfe6ff; }
  .chart-label { position: absolute; right: 260px; width: 92px; text-align: right; white-space: nowrap; }
  .chart-bar { position: absolute; left: 96px; top: 1px; height: 7px; background: #fff; }
  .chart-note { position: absolute; font-size: 5.5px; color: #fff; white-space: nowrap; }
  .chart-axis { position: absolute; left: 95px; top: 8px; width: 1px; height: 225px; background: #fff; }

  /* page 4 */
  .page-hospitals .top-band { position: absolute; left: 0; top: 0; }
  .page-hospitals .headline { left: 24px; top: 18px; font-size: 24px; color: #fff; font-weight: 500; }
  .page-hospitals .sub { left: 24px; top: 54px; font-size: 15px; color: #fff; }
  .page-hospitals .photo { left: 25px; top: 138px; width: 360px; height: 160px; background: linear-gradient(180deg,#a8c4e0,#d7dde3 45%,#7f8c94); }
  .page-hospitals .kiosk { left: 30px; top: 305px; width: 82px; height: 195px; }
  .table-title { left: 132px; top: 312px; font-family: "Oswald", sans-serif; font-weight: 500; font-size: 10.5px; color: #333; }
  .hospital-table { left: 132px; top: 328px; width: 268px; background: var(--navy); font-size: 4.8px; }
  .hospital-table th { background: var(--navy-deep); padding: 2px 2px; font-weight: 700; }
  .hospital-table td { padding: 1.4px 2px; text-align: center; border-bottom: 1px solid rgba(255,255,255,.2); }
  .hospital-table td.row { text-align: right; width: 86px; }
  .hospital-table tr.total td { font-weight: 700; }
  .page-hospitals .brand { left: 282px; top: 478px; color: var(--navy); gap: 6px; }
  .page-hospitals .brand-mark { width: 18px; height: 18px; border-width: 2px; }
  .page-hospitals .brand-name { font-size: 12px; width: 95px; }
</style>
</head>
<body>

<section class="page page-travellers">
  <svg class="top-band" width="410" height="520" viewBox="0 0 410 520" aria-hidden="true">
    <path d="M0 0H410V125C320 165 190 170 0 150Z" fill="#dfe4f5"/>
    <path d="M0 150C190 170 320 165 410 125V140C320 178 180 182 0 162Z" fill="#ffffff"/>
    <path d="M0 162C180 182 320 178 410 140V150C300 190 170 192 0 172Z" fill="#6f9ee0"/>
  </svg>
  <h1 class="headline abs">Movies for Travellers</h1>
  <p class="sub abs">Download Movies in under 3 minutes<br>No Internet Connection Required</p>
  <div class="brand abs"><span class="brand-mark"></span><span class="brand-name">Brightwell Amusements</span></div>
  <div class="placeholder photo" role="img" aria-label="Photo of a movie kiosk standing in a busy airport terminal hall"></div>
</section>

<section class="page page-airports">
  <h1 class="headline abs">Coming Soon to</h1>
  <h1 class="headline abs second">Airports Across Australia</h1>
  <div class="placeholder map" role="img" aria-label="Map of Australia with airport locations marked"></div>
  <ul class="bullets abs">
    <li>Current technology allows up to 10,000 encrypted digital movies to be stored on a kiosk.</li>
    <li>Multiple customers can simultaneously browse and rent movies on the kiosks FREE Wifi.</li>
    <li>Travellers are always killing time waiting to board their flight. Perfect time to browse movies.</li>
    <li>Target of 1 million transactions in the first 12 months.</li>
  </ul>
  <div class="placeholder kiosk" role="img" aria-label="Illustration of the Movies for Travellers kiosk"></div>
  <p class="stat abs">145,000,000+ Passenger Movements<br>for YE Feb 2014. Up 3.1% on 2013</p>
  <p class="stat-note abs">New Airport announced for Western Sydney to cope with increase demand.</p>
  <table class="data-table airport-table abs">
    <tr><td>SYDNEY</td><td class="num">38 437 727</td><td>MELBOURNE</td><td class="num">30 404 074</td></tr>
    <tr><td>BRISBANE</td><td class="num">21 576 425</td><td>PERTH</td><td class="num">12 908 095</td></tr>
    <tr><td>ADELAIDE</td><td class="num">7 468 471</td><td>GOLD COAST</td><td class="num">5 789 886</td></tr>
    <tr><td>CAIRNS</td><td class="num">4 346 485</td><td>CANBERRA</td><td class="num">2 861 066</td></tr>
    <tr><td>HOBART</td><td class="num">2 098 416</td><td>DARWIN</td><td class="num">2 013 685</td></tr>
    <tr><td>TOWNSVILLE</td><td class="num">1 541 457</td><td>LAUNCESTON</td><td class="num">1 267 589</td></tr>
    <tr><td>WILLIAMTOWN</td><td class="num">1 208 189</td><td>MACKAY</td><td class="num">1 003 895</td></tr>
    <tr><td>SUNSHINE COAST</td><td class="num">891 302</td><td>KARRATHA</td><td class="num">764 137</td></tr>
    <tr><td>ROCKHAMPTON</td><td class="num">694 369</td><td>ALICE SPRINGS</td><td class="num">667 282</td></tr>
    <tr><td>GLADSTONE</td><td class="num">506 419</td><td>PORT HEDLAND</td><td class="num">491 274</td></tr>
  </table>
</section>

<section class="page page-global">
  <h1 class="headline abs">Technology Built for<br>Global Expansion</h1>
  <div class="placeholder map" role="img" aria-label="World map silhouette"></div>
  <p class="sub abs small">Top 20 Airports in the world exceeded 1.2 billion passengers in 2013</p>
  <p class="sub abs big">Incorporating Blazing Fast Wifi</p>
  <div class="chart abs">
    <div class="chart-axis"></div>
    <span class="chart-note" style="left:100px;top:8px;">Future Devices to Download SD Movies in a few seconds</span>
    <div class="chart-row" style="top:22px;width:352px;"><span class="chart-label">WiGig 802.11ad (2015) (7000 Mbps)</span><span class="chart-bar" style="width:240px;"></span></div>
    <div class="chart-row" style="top:46px;width:352px;"><span class="chart-label">Wifi 802.11ac (1300 Mbps)</span><span class="chart-bar" style="width:46px;"></span><span class="chart-note" style="left:150px;top:0;">Nova Phone 4 &amp; 5</span></div>
    <div class="chart-row" style="top:70px;width:352px;"><span class="chart-label">Wifi 802.11n (300 Mbps)</span><span class="chart-bar" style="width:11px;"></span><span class="chart-note" style="left:112px;top:0;">2013 Model Pulse Phone/Tab - Download SD Movies in Under 3 Minutes</span></div>
    <div class="chart-row" style="top:94px;width:352px;"><span class="chart-label">Wifi 802.11g (108 Mbps)</span><span class="chart-bar" style="width:4px;"></span></div>
    <div class="chart-row" style="top:118px;width:352px;"><span class="chart-label">NBN 100 (100 Mbps)</span><span class="chart-bar" style="width:4px;"></span></div>
    <div class="chart-row" style="top:142px;width:352px;"><span class="chart-label">NBN 50 (50 Mbps)</span><span class="chart-bar" style="width:2px;"></span></div>
    <div class="chart-row" style="top:166px;width:352px;"><span class="chart-label">NBN 25 (25 Mbps)</span><span class="chart-bar" style="width:1px;"></span></div>
    <div class="chart-row" style="top:190px;width:352px;"><span class="chart-label">NBN 12 (12 Mbps)</span><span class="chart-bar" style="width:1px;"></span></div>
    <div class="chart-row" style="top:214px;width:352px;"><span class="chart-label">ADSL 2+ (24 Mbps)</span><span class="chart-bar" style="width:1px;"></span></div>
  </div>
</section>

<section class="page page-hospitals">
  <svg class="top-band" width="410" height="125" viewBox="0 0 410 125" aria-hidden="true">
    <path d="M0 0H410V75C300 105 160 112 0 108Z" fill="#1f3a8c"/>
    <path d="M0 108C160 112 300 105 410 75V86C300 116 160 122 0 118Z" fill="#6f9ee0"/>
  </svg>
  <h1 class="headline abs">Movies in Hospitals</h1>
  <p class="sub abs">Download Movies in under 3 minutes<br>No Internet Connection Required</p>
  <div class="placeholder photo" role="img" aria-label="Photo of a modern hospital building with a car park"></div>
  <div class="placeholder kiosk" role="img" aria-label="Illustration of the movie kiosk"></div>
  <p class="table-title abs">Public and Private Hospitals, States and Territories, 2012-13</p>
  <table class="data-table hospital-table abs">
    <tr><th></th><th>NSW</th><th>Vic</th><th>Qld</th><th>WA</th><th>SA</th><th>Tas</th><th>ACT</th><th>NT</th><th>Total</th></tr>
    <tr><td class="row">Public hospitals</td><td></td><td></td><td></td><td></td><td></td><td></td><td></td><td></td><td></td></tr>
    <tr><td class="row">Public acute hospitals</td><td>218</td><td>149</td><td>166</td><td>88</td><td>78</td><td>22</td><td>3</td><td>5</td><td>729</td></tr>
    <tr><td class="row">Public psychiatric hospitals</td><td>7</td><td>1</td><td>4</td><td>2</td><td>2</td><td>1</td><td>0</td><td>0</td><td>17</td></tr>
    <tr><td class="row">Total public hospitals</td><td>225</td><td>150</td><td>170</td><td>90</td><td>80</td><td>23</td><td>3</td><td>5</td><td>746</td></tr>
    <tr><td class="row">Private hospitals</td><td></td><td></td><td></td><td></td><td></td><td></td><td></td><td></td><td></td></tr>
    <tr><td class="row">Private free-standing day</td><td>96</td><td>85</td><td>52</td><td>35</td><td>26</td><td>8</td><td>0</td><td>0</td><td>311</td></tr>
    <tr><td class="row">Other private hospitals</td><td>89</td><td>79</td><td>53</td><td>22</td><td>28</td><td>6</td><td>0</td><td>0</td><td>281</td></tr>
    <tr><td class="row">Total private hospitals</td><td>185</td><td>164</td><td>105</td><td>57</td><td>54</td><td>14</td><td>0</td><td>0</td><td>592</td></tr>
    <tr class="total"><td class="row">All hospitals</td><td>410</td><td>314</td><td>275</td><td>147</td><td>134</td><td>37</td><td>3</td><td>5</td><td>1,338</td></tr>
  </table>
  <div class="brand abs"><span class="brand-mark"></span><span class="brand-name">Brightwell Amusements</span></div>
</section>

</body>
</html>
```